Brisk Venture - Logo & Business Card

I have briefly designed a logo for my small events business and need it fixed up. I would prefer it to be white on black background. I also need a PDF for business cards, I would like them to be black with the logo on one side and my details on the other side:

Brisk Venture
Corinna-May Feltwell
Founder / Director
0471 820 237
corinna@briskventure.com.au

```html
<!DOCTYPE html>
<html lang="en">
<head>
<meta charset="utf-8">
<title>Brisk Venture – Logo &amp; Business Card</title>
<link rel="stylesheet" href="https://fonts.googleapis.com/css2?family=PT+Sans&family=Share+Tech+Mono&display=swap">
<style>
  :root {
    --page: #ffffff;
    --ink: #000000;
    --card: #000000;
    --card-text: #ffffff;
    --accent: #84cbd3;
    --brand: #5ccac3;
  }
  html, body {
    margin: 0;
    padding: 0;
    overflow: hidden;
    background: var(--page);
  }
  .sheet {
    position: relative;
    width: 1200px;
    height: 1000px;
    background: var(--page);
    overflow: hidden;
  }
  .section-title {
    position: absolute;
    left: 0;
    width: 100%;
    margin: 0;
    text-align: center;
    font-family: "PT Sans", sans-serif;
    font-weight: 400;
    font-size: 62px;
    line-height: 1;
    color: var(--ink);
    letter-spacing: -0.5px;
  }
  .section-title--cards { top: 152px; left: -15px; }
  .section-title--logo { top: 670px; }
  .card {
    position: absolute;
    top: 246px;
    width: 533px;
    height: 307px;
    background: var(--card);
  }
  .card--front { left: 43px; }
  .card--back { left: 619px; }
  .brand-lockup {
    position: absolute;
    display: flex;
    align-items: center;
    gap: 10px;
    font-family: "Share Tech Mono", monospace;
    color: var(--brand);
    white-space: nowrap;
  }
  .brand-lockup__dot {
    display: block;
    border-radius: 50%;
    background: var(--brand);
  }
  .card--front .brand-lockup {
    left: 50%;
    top: 50%;
    transform: translate(-50%, -50%);
    font-size: 30px;
  }
  .card--front .brand-lockup__dot { width: 22px; height: 22px; }
  .details {
    position: absolute;
    left: 41px;
    top: 52px;
    margin: 0;
    font-family: "Share Tech Mono", monospace;
    font-size: 24px;
    line-height: 33px;
    color: var(--card-text);
  }
  .details p { margin: 0; }
  .details .name { color: var(--accent); }
  .details .contact { margin-top: 33px; }
  .logo-tile {
    position: absolute;
    left: 500px;
    top: 759px;
    width: 200px;
    height: 200px;
    background: var(--card);
  }
  .logo-tile .brand-lockup {
    left: 50%;
    top: 50%;
    transform: translate(-50%, -50%);
    font-size: 20px;
    gap: 7px;
  }
  .logo-tile .brand-lockup__dot { width: 14px; height: 14px; }
</style>
</head>
<body>
  <main class="sheet">
    <h2 class="section-title section-title--cards">BUSINESS CARD</h2>

    <section class="card card--front" aria-label="Business card front">
      <div class="brand-lockup">
        <span class="brand-lockup__dot"></span>
        <span class="brand-lockup__name">Brisk Venture</span>
      </div>
    </section>

    <section class="card card--back" aria-label="Business card back">
      <div class="details">
        <p class="company">Brisk Venture</p>
        <p class="name">Corinna-May Feltwell</p>
        <p class="role">Founder / Director</p>
        <div class="contact">
          <p class="phone">0471 820 237</p>
          <p class="email">corinna@briskventure.com.au</p>
        </div>
      </div>
    </section>

    <h2 class="section-title section-title--logo">LOGO</h2>

    <section class="logo-tile" aria-label="Logo">
      <div class="brand-lockup">
        <span class="brand-lockup__dot"></span>
        <span class="brand-lockup__name">Brisk Venture</span>
      </div>
    </section>
  </main>
</body>
</html>
```